EXPEDITE! Business Card For a Private Equity Firm
Fresh and Sleek
EXPEDITE!  Business Card For a Private Equity Firm - Financial Services
Creative Brief
Bright & Fun-filled
Ned Rusholt
Managing Partner
712 Larkmoor Street New York, NY 10032
ned@vorumbra-example.com
www.vorumbra-example.com
Looking for a fresh look on our new business cards. We have had previous designs on Plenavox for similar companies, but, now is time to refresh the look! Please submit as many design as possible. We will give you fast, efficient feedback!
Vorumbra Vorumbra
All. We also need email signatures and letterhead. Please provide.

```html
<!DOCTYPE html>
<html lang="en">
<head>
<meta charset="utf-8">
<title>Vorumbra Business Cards</title>
<link rel="stylesheet" href="https://fonts.googleapis.com/css2?family=Cinzel:wght@500&family=Questrial&display=swap">
<style>
  :root {
    --bg: #e4e5e7;
    --navy-deep: #0a2250;
    --navy: #123a7c;
    --blue: #1f5bb0;
    --blue-bright: #2f74cf;
    --white: #ffffff;
    --paper: #f4f5f6;
    --grey-band: #8e9298;
    --grey-band-dark: #6f737a;
    --ink-blue: #1d4f9c;
    --text-light: #dbe7f7;
  }
  * { box-sizing: border-box; margin: 0; padding: 0; }
  html, body {
    width: 1200px; height: 840px; overflow: hidden;
    background: var(--bg);
  }
  .sheet {
    width: 1200px; height: 840px;
    display: flex; align-items: center; justify-content: center; gap: 40px;
  }
  .card {
    width: 540px; height: 309px; position: relative; overflow: hidden;
    box-shadow: 0 10px 28px rgba(0,0,0,.18);
  }

  /* Back card: details */
  .card-back { display: flex; background: var(--paper); }
  .back-brand {
    width: 236px; display: flex; flex-direction: column;
    align-items: center; justify-content: center; gap: 14px;
  }
  .brand-dot {
    width: 46px; height: 46px; border-radius: 50%;
    background: radial-gradient(circle at 35% 35%, var(--blue-bright), var(--navy));
  }
  .brand-name {
    font-family: "Cinzel", serif; font-weight: 500;
    font-size: 27px; letter-spacing: 1px; color: var(--ink-blue);
  }
  .url-band {
    width: 38px; background: linear-gradient(90deg, var(--grey-band), var(--grey-band-dark));
    display: flex; align-items: center; justify-content: center;
  }
  .url-band span {
    transform: rotate(-90deg); white-space: nowrap;
    font-family: "Questrial", sans-serif; font-size: 12px;
    letter-spacing: 1px; color: var(--white);
  }
  .back-details {
    flex: 1; padding: 34px 26px 0 30px;
    background: linear-gradient(160deg, var(--blue) 0%, var(--navy) 60%, var(--navy-deep) 100%);
    color: var(--text-light); font-family: "Questrial", sans-serif;
  }
  .person-name { font-size: 21px; color: var(--white); }
  .person-role { font-size: 12px; margin-top: 3px; }
  .address { font-size: 13px; line-height: 1.35; margin-top: 42px; }
  .contact-list { list-style: none; margin-top: 12px; font-size: 12.5px; line-height: 1.6; }
  .contact-list li { display: flex; align-items: center; gap: 8px; }
  .contact-list svg { width: 12px; height: 12px; flex: none; }

  /* Front card: brand */
  .card-front {
    background: radial-gradient(ellipse at 25% 30%, var(--blue-bright) 0%, var(--blue) 25%, var(--navy) 60%, var(--navy-deep) 100%);
  }
  .front-brand {
    position: absolute; right: 42px; top: 150px; text-align: right;
  }
  .front-brand .brand-row { display: flex; align-items: center; gap: 12px; justify-content: flex-end; }
  .front-brand .brand-dot { width: 30px; height: 30px; background: var(--white); opacity: .9; }
  .front-brand .brand-name { color: var(--white); font-size: 34px; letter-spacing: 2px; }
  .front-url {
    font-family: "Questrial", sans-serif; font-size: 11px;
    letter-spacing: 2px; color: var(--text-light); margin-top: 4px;
  }
</style>
</head>
<body>
<main class="sheet">

  <section class="card card-back" aria-label="Business card back">
    <div class="back-brand">
      <div class="brand-dot"></div>
      <div class="brand-name">VORUMBRA</div>
    </div>
    <div class="url-band"><span>www.vorumbra-example.com</span></div>
    <div class="back-details">
      <p class="person-name">Ned Rusholt</p>
      <p class="person-role">Managing Partner</p>
      <p class="address">712 Larkmoor Street<br>New York, NY 10032</p>
      <ul class="contact-list">
        <li>
          <svg viewBox="0 0 12 12" aria-hidden="true"><path d="M3 1 L5 3.5 L4 5 Q5 7 7 8 L8.5 7 L11 9 L9.5 11 Q5 11 1 3 Z" fill="#dbe7f7"/></svg>
          (555) 014-2270
        </li>
        <li>
          <svg viewBox="0 0 12 12" aria-hidden="true"><rect x="3" y="1" width="6" height="4" fill="none" stroke="#dbe7f7"/><rect x="1" y="5" width="10" height="5" rx="1" fill="#dbe7f7"/><rect x="3" y="8" width="6" height="3" fill="#123a7c"/></svg>
          (555) 014-2280
        </li>
        <li>
          <svg viewBox="0 0 12 12" aria-hidden="true"><rect x="1" y="2.5" width="10" height="7" fill="none" stroke="#dbe7f7"/><path d="M1 2.5 L6 6.5 L11 2.5" fill="none" stroke="#dbe7f7"/></svg>
          ned@vorumbra-example.com
        </li>
      </ul>
    </div>
  </section>

  <section class="card card-front" aria-label="Business card front">
    <div class="front-brand">
      <div class="brand-row">
        <div class="brand-dot"></div>
        <div class="brand-name">VORUMBRA</div>
      </div>
      <p class="front-url">www.vorumbra-example.com</p>
    </div>
  </section>

</main>
</body>
</html>
```